Strelcor View VDI Brochure Design for IT Company

We are looking for an 4 page A4 brochure (A3 size folded in half).

We are an IT company based in Adelaide Australia and are promoting Strelcor Virtual Desktop Environments to medical practices (small, medium and large). As doctors and practice managers do not like to receive cold sales calls or emails - we would like to design up a 'high quality' brochure that will grab their attention!

The brochure will be mailed out and directed to practice managers - so the front page need to be captivating.

I will upload some text that we have come up with - this may not be the final wording, but will get the ball rolling. The 'amount' of text / dot points will be similar.

We would like to include quite a few pictures, because no one wants to read though a pile of text all piled together.

The text needs to be separated into "easy-to-read" sections throughout the brochure, highlighting on important aspects. For example the customer testimonials, The 'Happy' section, 'from ANY computer or device ANYTIME' etc.

Our traditional colour scheme can be found on our website at www.nimbletrail.com.au, however we are not too fussed for this project - as long as our logos are prominent throughout the design.

I have included several 'sample' images - basically just ones that were found on Findlo images + a few we took ourselves. Feel free to find and/or use your alternate images.

We definitely need to use pictures that feature doctor(s) using an Tabrio - this should maybe be the focus on the front cover. We would also like a close-up picture of an Tabrio inside with the medical software superimposed onto the screen (we have taken our own photo - but it's not great, and also uploaded a screen-shot of the medical software to superimpose on a higher quality Tabrio photo stock).

A couple of the pictures we would like to be prominent are the qOLM client (or more so the size of it - the picture with the client in someone’s hand. And the Tabrio picture(s) - doctors will like the ability to work from an Tabrio for anywhere.

Included are a selection of our company logos - these can be modified to suit whatever colour scheme you design.

Thanks in advance - Mark.

Target Market(s)

Doctors and Practice Managers of Medical and Health Centres

Industry/Entity Type

Computer

Requirements
Must have
• Pictures of doctors using Tabrios
Pictures of the QOLM client with the hand under it (to show the size)
Separated text blocks/sections for readability

```html
<!DOCTYPE html>
<html lang="en">
<head>
<meta charset="utf-8">
<title>NimbleTrail Strelcor Brochure</title>
<link href="https://fonts.googleapis.com/css2?family=Open+Sans:wght@300;400;600;700&display=swap" rel="stylesheet">
<style>
:root{
  --stage:#7d7d7d;
  --ink-dark:#0d0f12;
  --ink-mid:#1c1f24;
  --brand-blue:#3f8fd2;
  --brand-blue-soft:#5aa4de;
  --column-blue:#4b96d6;
  --paper:#ffffff;
  --text-grey:#5a5f66;
  --text-light:#c9ccd1;
}
*{box-sizing:border-box;margin:0;padding:0}
html,body{width:849px;height:1200px;overflow:hidden}
body{background:var(--stage);font-family:"Open Sans",Arial,sans-serif;position:relative}
.spread{position:absolute;left:0;width:849px;overflow:hidden}
.spread--outer{top:10px;height:560px;background:var(--ink-dark)}
.spread--inner{top:598px;height:602px}
.page{position:absolute;top:0;height:100%;width:424px}
.page--back{left:0;background:linear-gradient(160deg,#15181d,#07080a)}
.page--front{left:425px;background:radial-gradient(ellipse at 40% 40%,#1d2735 0%,#0a0c10 70%)}
.intro{position:absolute;left:34px;top:40px;width:190px;font-size:7.5px;line-height:1.45;color:var(--text-light)}
.intro strong{color:var(--brand-blue);font-weight:700}
.contact{position:absolute;left:34px;top:160px;width:220px;font-size:7.5px;line-height:1.5;color:var(--text-light)}
.contact h3{color:var(--brand-blue);font-size:9px;font-weight:700;margin-bottom:4px}
.contact .web{display:block;margin-top:10px;color:#fff;font-weight:700;font-size:10px}
.brand{position:absolute;right:36px;top:118px;display:flex;align-items:center;gap:8px}
.brand__mark{width:24px;height:24px;background:var(--brand-blue)}
.brand__name{color:#fff;font-size:21px;font-weight:400;line-height:1}
.brand__sub{position:absolute;right:36px;top:143px;color:var(--text-light);font-size:6px;letter-spacing:2px}
.light-streak{position:absolute;left:-120px;top:150px;width:700px;height:240px}
.device-photo{position:absolute;right:10px;bottom:40px;width:230px;height:220px;border-radius:6px;
  background:linear-gradient(145deg,#e9ebee 0%,#b9bdc3 55%,#50555c 100%)}
.page--inner-left{left:0;background:var(--ink-mid)}
.tablet-photo{position:absolute;left:30px;top:22px;width:290px;height:400px;border-radius:18px;
  background:linear-gradient(160deg,#3b3f46,#0e0f12)}
.tablet-screen{position:absolute;left:56px;top:52px;width:238px;height:340px;background:#24282f;padding:10px;
  color:var(--text-light);font-size:6px;line-height:1.5}
.qa-list{width:104px;float:left}
.qa-list li{list-style:none;margin-bottom:7px}
.qa-list b{color:var(--brand-blue-soft)}
.qa-side{width:108px;float:right;font-size:6px}
.qa-side h4{color:#fff;font-size:7.5px;margin-bottom:4px}
.doctors-photo{position:absolute;left:10px;bottom:12px;width:150px;height:100px;
  background:linear-gradient(135deg,#c7d6e4,#6f8aa3)}
.how h2{position:absolute;left:22px;top:455px;color:var(--brand-blue);font-weight:300;font-size:23px}
.how p{position:absolute;left:22px;top:492px;width:380px;font-size:6px;line-height:1.5;color:#a4a8ae}
.page--inner-right{left:425px;background:var(--paper)}
.benefits{position:absolute;left:0;top:0;width:128px;height:100%;background:var(--column-blue);padding:14px 10px;color:#fff}
.benefits h2{font-size:19px;font-weight:300;line-height:1.1;margin-bottom:6px}
.benefits ul{font-size:5.8px;line-height:1.45;margin-bottom:48px;padding-left:8px}
.why{position:absolute;left:140px;top:14px;width:270px}
.why h2,.feedback h2{color:var(--brand-blue);font-weight:300;font-size:19px;line-height:1.1}
.why .cols{display:flex;gap:10px;margin-top:10px;font-size:5.8px;line-height:1.5;color:var(--text-grey)}
.why .cols div{flex:1}
.feedback{position:absolute;left:140px;top:350px;width:100px}
.feedback blockquote{color:var(--brand-blue);font-size:8px;line-height:1.35;margin-top:10px}
.story{position:absolute;left:252px;top:350px;width:158px;font-size:5.8px;line-height:1.5;color:var(--text-grey)}
.story p{margin-bottom:6px}
</style>
</head>
<body>

<section class="spread spread--outer">
  <div class="page page--back">
    <p class="intro"><strong>NimbleTrail IT</strong> was founded in Adelaide and has been specialising in IT care for over ten years. Supporting doctors in the health sector, we deliver systems to medical practices across the state, as a leader in the field. We provide complete managed service packages for health practices of every size and keep teams focused on patients, not servers. Ask us how our clients benefit from a simpler desktop today.</p>
    <div class="contact">
      <h3>NimbleTrail IT Consulting</h3>
      14 Harbour Lane, Westfield SA 5099<br>
      Phone (08) 7000 4100 · Facsimile (08) 7000 4199<br>
      hello@nimbletrail.com.au
      <span class="web">www.nimbletrail.com.au</span>
    </div>
  </div>
  <div class="page page--front">
    <svg class="light-streak" viewBox="0 0 700 240" aria-hidden="true">
      <defs>
        <linearGradient id="streak" x1="0" x2="1">
          <stop offset="0" stop-color="#3f8fd2" stop-opacity="0"/>
          <stop offset=".6" stop-color="#7fbef0" stop-opacity=".8"/>
          <stop offset="1" stop-color="#3f8fd2" stop-opacity="0"/>
        </linearGradient>
      </defs>
      <path d="M0 200 Q300 120 700 20" stroke="url(#streak)" stroke-width="6" fill="none"/>
      <path d="M0 215 Q320 140 700 50" stroke="url(#streak)" stroke-width="2" fill="none"/>
      <path d="M0 230 Q340 160 700 80" stroke="url(#streak)" stroke-width="1" fill="none"/>
    </svg>
    <div class="brand"><span class="brand__mark"></span><span class="brand__name">NimbleTrail</span></div>
    <span class="brand__sub">IT CONSULTING</span>
    <div class="device-photo" role="img" aria-label="Photo of the small white qOLM client unit with front ports"></div>
  </div>
</section>

<section class="spread spread--inner">
  <div class="page page--inner-left">
    <div class="tablet-photo" role="img" aria-label="Photo of a Tabrio tablet held in hand"></div>
    <div class="tablet-screen">
      <ul class="qa-list">
        <li><b>Q1</b> Why choose Strelcor for your practice?</li>
        <li><b>Q2</b> Can staff log in from a Tabrio at home?</li>
        <li><b>Q3</b> Running clinical software on any device?</li>
        <li><b>Q4</b> Keeping patient records safe and backed up?</li>
        <li><b>Q5</b> What does it cost to get started?</li>
      </ul>
      <div class="qa-side">
        <h4>Strelcor View for Medical Practitioners</h4>
        Access your desktop from any computer or device, anytime, with the same apps and files you use every day at the clinic.
        <h4 style="margin-top:8px">Want to be able to work from anywhere?</h4>
        Log on from the ward, the office or home.
      </div>
      <div class="doctors-photo" role="img" aria-label="Photo of doctors reviewing notes on a Tabrio"></div>
    </div>
    <div class="how">
      <h2>How does it work?</h2>
      <p>Strelcor View moves each desktop off the local computer and into a secure central server. Staff connect through a small qOLM client or a Tabrio, and see their full desktop with all clinical programs, just as before. Updates, backups and security are handled once on the server instead of on every machine, so there is less to break and less to manage. If a device fails, simply swap it and log back in within minutes. Practices save power, space and support time while gaining the freedom to work from any room, any site or from home, with patient data never leaving the secure practice network.</p>
    </div>
  </div>

  <div class="page page--inner-right">
    <aside class="benefits">
      <h2>Doctors Happy</h2>
      <ul><li>Access records from any room</li><li>Log in from a Tabrio at home</li><li>Same desktop every time</li><li>Faster start up each morning</li></ul>
      <h2>Management Happy</h2>
      <ul><li>Lower hardware and power cost</li><li>One place to update and back up</li><li>Predictable monthly pricing</li></ul>
      <h2>Admin Staff Happy</h2>
      <ul><li>Quiet, compact desk units</li><li>Fewer crashes and delays</li><li>Help just a call away</li></ul>
    </aside>
    <div class="why">
      <h2>Why Choose<br>Strelcor?</h2>
      <div class="cols">
        <div>Strelcor is a proven platform used by clinics across the country. It centralises every desktop so your practice runs on one secure, managed system. New staff can be set up in minutes, and there is no need to buy a new computer every few years. Clients connect over the network with high speed and full clinical software support.</div>
        <div>Security is built in: data stays on the server, not on the device, so a lost Tabrio never means lost records. Automatic backups run each night and recovery is fast. Our team monitors the system around the clock and resolves most issues before staff even notice them.</div>
      </div>
    </div>
    <div class="feedback">
      <h2>Feedback from clients:</h2>
      <blockquote>"Why didn't we do this years ago?"</blockquote>
      <blockquote>"I love being able to access my medical software on my Tabrio wherever I am."</blockquote>
      <blockquote>"Printing from home saves me a lot of time."</blockquote>
    </div>
    <div class="story">
      <p>Since moving to Strelcor our practice has seen fewer support calls and far less downtime. Our doctors were quick to adopt the new setup.</p>
      <p>NimbleTrail IT Consulting made the change simple. The team planned each step, trained our staff and stayed on site during the first week to answer questions.</p>
      <p>We now run three clinics from one system, and moving staff between sites takes no extra setup at all.</p>
      <p>The qOLM clients are tiny, silent and use a fraction of the power of our old machines. Our reception desks have never looked tidier.</p>
    </div>
  </div>
</section>

</body>
</html>
```